Graphic design of labels for scented candles

Following a change in our team structure, a deadline was put in place and the brief changed.
We need a beautiful label for our candles, one that sticks *all around the glass*. Must obviously include our logo as well as the description of the perfume.
The clientele is mainly female, between 35 and 65 years old, of a classic nature.
Brand values:
Feminine
Warm-joyful
Sophisticated-elegant
Eco-friendly, pet-friendly
Natural
Inspires confidence.
The idea is to have something different, the final appearance must be elegant and refined, which will be your challenge given the shape.

What we need:
- changeable colors
- small transparent elements which can be printed on a gold or silver paper background (example: logo, frame, elements, etc.)

- the logo (black or very dark gray) must be present + text "vegetable candle", then the perfume and below:
vegetable wax - handcrafted"
I am attaching a picture of our current labels to the files.
For the size I'll let you manage.
These labels can also be assigned to derived products such as room fragrances, pillow mists, etc.
The brand targets the middle class and above.
For the fonts I leave the choice to you.
Thank you and good luck to all !

Update: there is no longer a cat's head as a background shape, you have free choice.
THANKS

Target Market(s)

Women aged 35 to 65

Industry/Entity Type

Industrie du Parfum

Colors
00AB8E
00BBA5
67D7C9
C6EFE9
E9F9F6
59FF00
82FF00
B8FF75
E3FFCB
F4FFEA
FFF300
FFF600
FEFA6F
FFFEC7
FFFEE8
FFC000
F8CF3A
FAE287
FDF2CF
FEFAEE
F0912C
F2A743
F7CA91
FBE8D2
FDF5EE
EE7325
F08F49
F5BC92
FAE3D3
FDF4ED
EB3D1F
EC4F4E
F09395
F8D3D4
FCEDEE
E54698
E96AAD
F1A4CE
F9D9EA
FCEFF6
A7469A
B969AE
D3A5CF
EDDBEB
F8F0F9
6B429C
8869AF
B7A5CE
E3DAEB
F3F0F8

Requirements
Must have
• modifiable colors - small transparent elements which can be printed on a gold or silver paper background (example: frame, elements, etc.) - the logo (black or very dark gray) must be present + text "vegetable candle, then the perfume and below: vegetable wax - handcrafted"
Nice to have
• Elements that could be made transparent (logo text frame) to be able to edit on gold papers and give a luxurious appearance
Should not have
• no childish appearance.

```html
<!DOCTYPE html>
<html lang="en">
<head>
<meta charset="utf-8">
<title>Lumara Candle – Labels</title>
<link href="https://fonts.googleapis.com/css2?family=Montserrat:wght@400;500;700&display=swap" rel="stylesheet">
<style>
  :root {
    --page: #ffffff;
    --rose: #e54698;
    --aqua: #67d7c9;
    --light-ink: #ffffff;
    --dark-ink: #111111;
  }
  html, body {
    margin: 0;
    padding: 0;
    width: 1200px;
    height: 892px;
    overflow: hidden;
    background: var(--page);
    font-family: "Montserrat", sans-serif;
  }
  .canvas {
    position: relative;
    width: 1200px;
    height: 892px;
  }
  .label {
    position: absolute;
    top: 278px;
    width: 474px;
    height: 332px;
  }
  .label--rose { left: 95px; --fill: var(--rose); --ink: var(--light-ink); }
  .label--aqua { left: 628px; --fill: var(--aqua); --ink: var(--dark-ink); }
  .label__shape {
    position: absolute;
    inset: 0;
    width: 474px;
    height: 332px;
  }
  .label__body { fill: var(--fill); }
  .label__ring { fill: none; stroke: var(--ink); stroke-width: 3.5; }
  .label__text {
    position: absolute;
    left: 0;
    width: 474px;
    text-align: center;
    color: var(--ink);
    margin: 0;
    white-space: nowrap;
  }
  .brand-name {
    top: 130px;
    font-size: 64px;
    font-weight: 500;
    line-height: 1;
    letter-spacing: 1px;
  }
  .brand-line {
    top: 216px;
    display: flex;
    justify-content: center;
    align-items: center;
    gap: 12px;
    font-size: 21px;
    font-weight: 400;
    letter-spacing: 12px;
    line-height: 1;
  }
  .brand-line__rule {
    display: block;
    width: 36px;
    height: 1px;
    background: var(--ink);
  }
  .product-type {
    top: 249px;
    font-size: 15px;
    font-weight: 700;
    line-height: 1;
  }
  .product-notes {
    top: 270px;
    font-size: 11.5px;
    font-weight: 400;
    letter-spacing: 0.6px;
    line-height: 1;
  }
</style>
</head>
<body>
<main class="canvas">

  <section class="label label--rose">
    <svg class="label__shape" viewBox="0 0 474 332" aria-hidden="false">
      <defs>
        <clipPath id="rose-clip"><rect x="0" y="0" width="474" height="332" rx="70"/></clipPath>
      </defs>
      <rect class="label__body" x="0" y="0" width="474" height="332" rx="70" role="img" aria-label="Die-cut label shape in the form of a cat head with ears and whiskers"/>
      <g clip-path="url(#rose-clip)">
        <circle class="label__ring" cx="237" cy="166" r="176"/>
      </g>
    </svg>
    <p class="label__text brand-name">Lumara</p>
    <p class="label__text brand-line"><span class="brand-line__rule"></span>CANDLE<span class="brand-line__rule"></span></p>
    <p class="label__text product-type">vegetable candle</p>
    <p class="label__text product-notes">vegetable wax - handcrafted</p>
  </section>

  <section class="label label--aqua">
    <svg class="label__shape" viewBox="0 0 474 332" aria-hidden="false">
      <defs>
        <clipPath id="aqua-clip"><rect x="0" y="0" width="474" height="332" rx="70"/></clipPath>
      </defs>
      <rect class="label__body" x="0" y="0" width="474" height="332" rx="70" role="img" aria-label="Die-cut label shape in the form of a cat head with ears and whiskers"/>
      <g clip-path="url(#aqua-clip)">
        <circle class="label__ring" cx="237" cy="166" r="176"/>
      </g>
    </svg>
    <p class="label__text brand-name">Lumara</p>
    <p class="label__text brand-line"><span class="brand-line__rule"></span>CANDLE<span class="brand-line__rule"></span></p>
    <p class="label__text product-type">vegetable candle</p>
    <p class="label__text product-notes">vegetable wax - handcrafted</p>
  </section>

</main>
</body>
</html>
```